Business Card Design Project

I want a design for my business cards based on an excisting logo design.

Target Market(s)

Marketeers, PR-peeps, CEO's, decisionmakers, entrepreneurs

Industry/Entity Type

Business

Requirements
Nice to have
• Some visual interest on the back too
Should not have
• Sarif on the font

```html
<!DOCTYPE html>
<html lang="nl">
<head>
<meta charset="utf-8">
<title>Verdalia PR – visitekaartjes</title>
<link rel="stylesheet" href="https://fonts.googleapis.com/css2?family=Open+Sans:wght@400;600;700&display=swap">
<style>
  :root {
    --bg: #e9e7e3;
    --card-white: #ffffff;
    --card-grey: #ececec;
    --ink: #222222;
    --logo-grey: #6d6e70;
    --green-bright: #8cc63f;
    --green-light: #b5dc6a;
    --green-mid: #4fae3a;
    --green-deep: #2f8f2f;
    --faint: #dcdcdc;
  }
  * { box-sizing: border-box; margin: 0; padding: 0; }
  html, body { width: 1200px; height: 951px; overflow: hidden; }
  body {
    background: var(--bg);
    font-family: "Open Sans", Arial, sans-serif;
    position: relative;
  }
  .card {
    position: absolute;
    width: 620px;
    height: 400px;
    border-radius: 26px;
    overflow: hidden;
    box-shadow: 0 10px 28px rgba(0,0,0,.22);
  }
  .card--front {
    left: 80px; top: 70px;
    background: linear-gradient(90deg, var(--card-white) 0%, var(--card-grey) 100%);
  }
  .card--back {
    left: 500px; top: 480px;
    background: var(--card-white);
  }
  .faint-circle {
    position: absolute;
    right: -70px; top: -90px;
    width: 380px; height: 380px;
    border-radius: 50%;
    background: var(--faint);
    opacity: .45;
  }
  .brand {
    position: absolute;
    display: flex;
    align-items: center;
    gap: 14px;
    color: var(--logo-grey);
    font-weight: 600;
    letter-spacing: .5px;
    white-space: nowrap;
  }
  .brand__dot {
    border-radius: 50%;
    background: var(--green-bright);
    flex: none;
  }
  .card--front .brand { left: 50px; top: 175px; font-size: 36px; }
  .card--front .brand__dot { width: 44px; height: 44px; }
  .card--back .brand { left: 40px; top: 60px; font-size: 32px; }
  .card--back .brand__dot { width: 40px; height: 40px; }
  .services {
    position: absolute;
    left: 345px; top: 168px;
    width: 200px;
    text-align: center;
    font-size: 15px;
    line-height: 1.3;
    color: var(--ink);
  }
  .wave { position: absolute; left: 0; top: 0; }
  .holder {
    position: absolute;
    right: 40px; top: 45px;
    font-size: 23px;
    font-weight: 700;
    color: var(--ink);
    letter-spacing: .5px;
  }
  .social {
    position: absolute;
    left: 36px; top: 300px;
    list-style: none;
    color: #fff;
    font-size: 17px;
    line-height: 1.35;
  }
  .contact {
    position: absolute;
    left: 330px; top: 238px;
    list-style: none;
    color: #fff;
    font-size: 16px;
    line-height: 1.35;
  }
  .contact li { display: flex; align-items: flex-start; gap: 10px; }
  .contact li + li { margin-top: 2px; }
  .contact .gap { margin-top: 16px; }
  .contact svg { flex: none; margin-top: 4px; }
</style>
</head>
<body>

  <section class="card card--front" aria-label="Voorzijde visitekaartje">
    <div class="faint-circle"></div>
    <div class="brand"><span class="brand__dot"></span>Verdalia PR</div>
    <p class="services">Systemisch en strategisch PR<br>Marketing<br>Communicatie advies</p>
  </section>

  <section class="card card--back" aria-label="Achterzijde visitekaartje">
    <svg class="wave" width="620" height="400" viewBox="0 0 620 400" aria-hidden="true">
      <defs>
        <linearGradient id="greenFill" x1="0" y1="0" x2="0" y2="1">
          <stop offset="0" stop-color="var(--green-mid)"/>
          <stop offset="1" stop-color="var(--green-deep)"/>
        </linearGradient>
      </defs>
      <path d="M0,238 C150,185 320,285 620,180 L620,400 L0,400 Z" fill="var(--green-light)"/>
      <path d="M0,258 C160,205 330,305 620,202 L620,400 L0,400 Z" fill="url(#greenFill)"/>
    </svg>

    <div class="brand"><span class="brand__dot"></span>Verdalia PR</div>
    <h1 class="holder">Lotte Brandsma</h1>

    <ul class="social">
      <li>updates.verdaliapr.nl</li>
      <li>community.verdaliapr.nl</li>
    </ul>

    <ul class="contact">
      <li>
        <svg width="14" height="13" viewBox="0 0 14 13" aria-hidden="true"><path d="M7 0 L14 6 H12 V13 H8.5 V9 H5.5 V13 H2 V6 H0 Z" fill="#fff"/></svg>
        <span>Lindeweg 12<br>6701 AB Ede</span>
      </li>
      <li class="gap">
        <svg width="14" height="14" viewBox="0 0 14 14" aria-hidden="true"><circle cx="7" cy="7" r="6.3" fill="none" stroke="#fff" stroke-width="1.4"/><path d="M4.5 3.5 L6 3.5 L6.5 5.5 L5.6 6.2 C6.1 7.3 6.8 8 7.8 8.4 L8.5 7.5 L10.5 8 L10.5 9.5 C7 10 4 7 4.5 3.5 Z" fill="#fff"/></svg>
        <span>+31(0)6 20481395</span>
      </li>
      <li>
        <svg width="14" height="13" viewBox="0 0 14 13" aria-hidden="true"><circle cx="7" cy="6.5" r="6.5" fill="#fff"/><rect x="3.5" y="4" width="7" height="5" fill="none" stroke="var(--green-mid)" stroke-width="1"/><path d="M3.5 4 L7 6.8 L10.5 4" fill="none" stroke="var(--green-mid)" stroke-width="1"/></svg>
        <span>lotte.brandsma@verdaliapr.nl</span>
      </li>
      <li>
        <svg width="14" height="14" viewBox="0 0 14 14" aria-hidden="true"><circle cx="7" cy="7" r="7" fill="#fff"/></svg>
        <span>www.verdaliapr.nl</span>
      </li>
    </ul>
  </section>

</body>
</html>
```